logo and label design for a vegan skincare Called Leafmerelle

We need a logo and label design for a skincare brand called leafmerelle based in Australia. The products are 100% natural, Australian made, small batch, vegan, cruelty-free, ethical and sustainable beauty products. The secret of our skin care products are their naturally active ingredients.
They are potent, yet incredibly gentle on sensitive skin. We believe in investing in only the highest quality and ethical ingredients to ensure we are creating products we can stand behind.
Our products use: Naturally delivered ingredients; Organic ingredients where is possible; Australian oils, fruits & Extracts; Aromatherapy oils; sustainable & ethical ingredients; natural preservatives.
Our products don't use: sulphates; parabens; phthalates; Petrochemicals; synthetic colours; synthetic fragrances. All label must be design for an amber bottle.
Label Requirements:
* 300 DPI minimum
* All fonts have been outlined
* 3mm Bleed included in artwork
Colors
Designer to choose colors to be used in the design.
Look and feel
Each slider illustrates characteristics of the customer's brand and the style your logo design should communicate.

```html
<!DOCTYPE html>
<html lang="en">
<head>
<meta charset="utf-8">
<title>Leafmerelle — Skincare Labels</title>
<link rel="stylesheet" href="https://fonts.googleapis.com/css2?family=Cormorant+Garamond:wght@500&family=Open+Sans+Condensed:wght@300&display=swap">
<style>
  :root {
    --canvas-bg: #f4f4f5;
    --label-paper: #fbfbf8;
    --ink-grey: #5f5f62;
    --ink-soft: #6c6c70;
    --lavender: #aeb0dc;
    --lavender-deep: #7d86c9;
    --blush: #f0c3cc;
    --coral: #d9676a;
  }
  * { box-sizing: border-box; margin: 0; padding: 0; }
  html, body { width: 1200px; height: 1200px; overflow: hidden; }
  body {
    background: var(--canvas-bg);
    position: relative;
    font-family: "Open Sans Condensed", "Arial Narrow", sans-serif;
    color: var(--ink-grey);
  }
  .label {
    position: absolute;
    background: var(--label-paper);
    box-shadow: 0 2px 10px rgba(0,0,0,0.08);
    overflow: hidden;
    text-align: center;
  }
  .label--cleanser { left: 166px; top: 430px; width: 382px; height: 622px; }
  .label--mask { left: 615px; top: 760px; width: 415px; height: 310px; }

  .marbling { position: absolute; left: 0; right: 0; }
  .marbling--cleanser-top {
    top: 0; height: 150px;
    background: linear-gradient(180deg, rgba(174,176,220,0.75) 0%, rgba(174,176,220,0.35) 55%, rgba(251,251,248,0) 100%);
  }
  .marbling--cleanser-bottom {
    bottom: 0; height: 230px;
    background: linear-gradient(0deg, rgba(174,176,220,0.7) 0%, rgba(174,176,220,0.3) 50%, rgba(251,251,248,0) 100%);
  }
  .marbling--mask-top {
    top: 0; height: 70px;
    background: linear-gradient(180deg, rgba(240,195,204,0.75) 0%, rgba(251,251,248,0) 100%);
  }

  .brand {
    position: absolute; left: 0; right: 0;
    font-family: "Cormorant Garamond", Georgia, serif;
    font-weight: 500;
    color: var(--ink-grey);
    letter-spacing: 0.5px;
    line-height: 1;
    display: flex; justify-content: center; align-items: center; gap: 8px;
  }
  .brand__dot {
    width: 14px; height: 14px; border-radius: 50%;
    background: var(--ink-soft);
  }
  .label--cleanser .brand { top: 206px; font-size: 52px; }
  .label--mask .brand { top: 104px; font-size: 50px; }

  .product-name {
    position: absolute; left: 0; right: 0;
    font-family: "Cormorant Garamond", Georgia, serif;
    font-variant: small-caps;
    font-weight: 500;
    letter-spacing: 3px;
    color: var(--ink-soft);
  }
  .label--cleanser .product-name { top: 282px; font-size: 17px; }
  .label--mask .product-name { top: 172px; font-size: 16px; }

  .swatch { position: absolute; height: 28px; border-radius: 3px 14px 14px 3px; }
  .label--cleanser .swatch {
    left: 116px; top: 313px; width: 170px;
    background: linear-gradient(90deg, var(--lavender-deep), #8e96d3 80%, rgba(142,150,211,0.3));
  }
  .label--mask .swatch {
    left: 144px; top: 200px; width: 145px; height: 24px;
    background: linear-gradient(90deg, var(--coral), #e0807d 80%, rgba(224,128,125,0.3));
  }

  .ingredients {
    position: absolute; left: 0; right: 0;
    font-weight: 300; text-transform: uppercase;
    color: #3d3d40;
  }
  .label--cleanser .ingredients { top: 362px; font-size: 21px; line-height: 33px; }
  .label--mask .ingredients { top: 240px; font-size: 19px; line-height: 23px; }

  .volume { position: absolute; left: 0; right: 0; color: #3d3d40; }
  .label--cleanser .volume { bottom: 24px; font-weight: 300; font-size: 19px; }
  .label--mask .volume {
    top: 312px; font-family: "Cormorant Garamond", Georgia, serif; font-size: 18px;
  }
</style>
</head>
<body>
  <section class="label label--cleanser">
    <div class="marbling marbling--cleanser-top" role="img" aria-label="Soft lavender watercolour marbling"></div>
    <div class="marbling marbling--cleanser-bottom" role="img" aria-label="Soft lavender watercolour marbling"></div>
    <div class="brand"><span>leafmerelle</span><span class="brand__dot"></span></div>
    <p class="product-name">Purifying Gel Cleanser</p>
    <div class="swatch" role="img" aria-label="Lavender paint brush stroke"></div>
    <p class="ingredients">Lemon Tea Tree<br>&amp; Vitamim E</p>
    <p class="volume">200ml</p>
  </section>

  <section class="label label--mask">
    <div class="marbling marbling--mask-top" role="img" aria-label="Soft pink watercolour marbling"></div>
    <div class="brand"><span>leafmerelle</span><span class="brand__dot"></span></div>
    <p class="product-name">Pink Clay Calming Mask</p>
    <div class="swatch" role="img" aria-label="Coral pink paint brush stroke"></div>
    <p class="ingredients">Calendula<br>Chamomile<br>Aloe Vera</p>
    <p class="volume">90g</p>
  </section>
</body>
</html>
```